I would like to start a new webpage for a dating site in switzerland.
The dating site is not a escort service at all and should not transmit any type of sexual connotation.
The is more a compagnionship dating : male pay to meet ladies for some time in which they invite them for dinner, coktail, museum visit or walking or even skying. the meeting will take place in big cities in switzerland: geneva, zurich, bern, lausannes.

Industry/Entity Type

Dating

```html
<!DOCTYPE html>
<html lang="en">
<head>
<meta charset="utf-8">
<title>Swiss Soirée – Find Your Companion</title>
<link href="https://fonts.googleapis.com/css2?family=Maven+Pro:wght@400;500&family=Open+Sans:wght@400;600&display=swap" rel="stylesheet">
<style>
:root{
  --ink:#3c3c3c;
  --teal:#1a8fb3;
  --pink:#e0146e;
  --grey-text:#8a8a8a;
  --band:#e8f1f5;
  --footer:#2e2e2e;
  --panel:rgba(58,62,66,.62);
  --field:rgba(40,44,48,.35);
  --btn:#2f2f2f;
}
*{box-sizing:border-box;margin:0;padding:0}
html,body{width:848px;height:1200px;overflow:hidden;background:#fff}
body{font-family:"Open Sans",Arial,sans-serif;color:var(--ink)}
.page{position:relative;width:848px;height:1200px;overflow:hidden}
.abs{position:absolute}

.hero{left:0;top:0;width:848px;height:548px;
  background:
    linear-gradient(180deg,rgba(240,244,247,.95) 0%,rgba(240,244,247,.55) 18%,rgba(240,244,247,0) 32%),
    linear-gradient(100deg,#b9aa98 0%,#c79a78 22%,#e2b48e 40%,#f1d3b4 55%,#9fb0b4 72%,#7e9ea6 86%,#c8c4c2 100%);}

.brand{left:62px;top:52px;display:flex;align-items:center;gap:14px}
.brand-dot{width:32px;height:32px;border-radius:50%;background:var(--teal)}
.brand-name{font-family:"Maven Pro",sans-serif;font-size:36px;font-weight:400;color:#555}

.login{left:728px;top:29px;width:58px;height:26px;background:var(--btn);border:1px solid #666;color:#fff;
  font-family:"Maven Pro",sans-serif;font-size:13px;display:flex;align-items:center;justify-content:center}
.nav{left:478px;top:72px;width:309px;height:34px;background:rgba(255,255,255,.55);
  display:flex;justify-content:space-around;align-items:center;padding:0 6px}
.nav a{font-family:"Maven Pro",sans-serif;font-size:13px;color:#444;text-decoration:none;letter-spacing:-.2px}

.finder{left:465px;top:204px;width:322px;height:280px;background:var(--panel);border:1px solid rgba(40,40,40,.6)}
.finder h2{position:absolute;left:0;right:0;top:20px;text-align:center;font-family:"Maven Pro",sans-serif;
  font-weight:400;font-size:22px;color:#fff;letter-spacing:-.3px}
.finder label{position:absolute;left:21px;font-family:"Maven Pro",sans-serif;font-size:12px;color:#fff;line-height:29px}
.field{position:absolute;height:29px;background:var(--field);border:1px solid #3a3a3a;color:#eee;
  font-size:10px;display:flex;align-items:center;padding-left:10px;white-space:nowrap;overflow:hidden}
.field.select::after{content:"";position:absolute;right:9px;top:12px;border:4px solid transparent;border-top:5px solid #ddd}
.to{position:absolute;left:177px;top:110px;font-size:10px;color:#eee;line-height:29px}
.search-btn{position:absolute;left:229px;top:238px;width:66px;height:26px;background:var(--btn);border:1px solid #555;
  color:#fff;font-family:"Maven Pro",sans-serif;font-size:12px;display:flex;align-items:center;justify-content:center}

.results-title{left:0;top:588px;width:848px;text-align:center;font-family:"Maven Pro",sans-serif;font-size:27px;
  color:var(--pink);font-weight:400}
.profile-card{left:60px;top:649px;width:117px;height:141px;background:#f4f9fb;border:1px solid #a9d5e6;text-align:center}
.profile-card .name{margin-top:12px;font-family:"Maven Pro",sans-serif;font-size:13px;color:var(--teal)}
.profile-card hr{border:0;border-top:1px solid #d7dfe2;margin:6px 10px 8px}
.profile-card p{font-family:"Maven Pro",sans-serif;font-size:11.5px;color:#777;line-height:23px}
.profile-card .links{display:flex;justify-content:center;gap:5px;margin-top:2px}
.profile-card .links span{width:16px;height:16px;border-radius:50%;background:#a9d5e6}
.member{width:115px;text-align:center}
.member .photo{width:115px;height:115px;border-radius:50%;border:1px solid #ddd}
.member .caption{margin-top:10px;font-family:"Maven Pro",sans-serif;font-size:14px;color:#666}

.band{left:0;top:841px;width:848px;height:273px;background:var(--band)}
.welcome h2,.why h2{font-family:"Maven Pro",sans-serif;font-weight:400;color:var(--teal)}
.welcome{left:61px;top:878px;width:440px}
.welcome h2{font-size:26px;margin-bottom:12px}
.welcome p{font-size:9.6px;line-height:18px;color:var(--grey-text);letter-spacing:-.25px;margin-bottom:4px}
.register{display:inline-flex;align-items:center;justify-content:center;width:111px;height:29px;margin-top:10px;
  background:var(--btn);color:#fff;font-family:"Maven Pro",sans-serif;font-size:12px}
.why{left:542px;top:880px;width:250px}
.why h2{font-size:22px;margin-bottom:13px}
.why p{font-size:9.6px;line-height:18px;color:var(--grey-text);letter-spacing:-.25px}
.why ul{list-style:none;margin-top:10px}
.why li{position:relative;padding-left:12px;font-size:11px;line-height:24px;color:var(--pink)}
.why li::before{content:"›";position:absolute;left:0;top:0;color:var(--pink)}

.footer{left:0;top:1114px;width:848px;height:86px;background:var(--footer)}
.footer-links{position:absolute;left:62px;top:22px;font-family:Arial,sans-serif;font-size:10.5px;color:#fff}
.copyright{position:absolute;left:62px;top:47px;font-family:Arial,sans-serif;font-size:10.5px;color:#fff}
.social{position:absolute;top:32px}
.social span{position:absolute;width:26px;height:26px;top:0}
</style>
</head>
<body>
<div class="page">

  <div class="abs hero" role="img" aria-label="Photo of a smiling couple resting their heads together by a canal with gondolas"></div>

  <div class="abs brand"><span class="brand-dot"></span><span class="brand-name">Swiss Soirée</span></div>
  <div class="abs login">LOGIN</div>
  <nav class="abs nav"><a>HOME</a><a>ABOUT US</a><a>MEMBERS</a><a>CONTACT</a></nav>

  <form class="abs finder">
    <h2>FIND YOUR COMPANION</h2>
    <label style="top:67px">Name:</label>
    <div class="field" style="left:67px;top:67px;width:228px">Enter your name</div>
    <label style="top:110px">Age:</label>
    <div class="field select" style="left:67px;top:110px;width:100px">Min Age</div>
    <span class="to">to</span>
    <div class="field select" style="left:195px;top:110px;width:100px">Max. Age</div>
    <label style="top:153px">Invite:</label>
    <div class="field select" style="left:67px;top:153px;width:228px">Dinner</div>
    <label style="top:198px">Place:</label>
    <div class="field select" style="left:67px;top:198px;width:228px">Zurich</div>
    <div class="search-btn">SEARCH</div>
  </form>

  <h2 class="abs results-title">SEARCH RESULTS</h2>

  <div class="abs profile-card">
    <div class="name">ELENA</div>
    <hr>
    <p>Age: 27<br>Place: Zurich<br>Germany</p>
    <div class="links"><span></span><span></span></div>
  </div>

  <div class="abs member" style="left:213px;top:649px">
    <div class="photo" role="img" aria-label="Portrait of a smiling woman with sunglasses on her head" style="background:radial-gradient(circle at 45% 40%,#c9a186,#6b4a3a 70%,#e6e1dc)"></div>
    <div class="caption">Nina Roth</div>
  </div>
  <div class="abs member" style="left:364px;top:649px">
    <div class="photo" role="img" aria-label="Portrait of a young woman with braided hair in a denim jacket" style="background:radial-gradient(circle at 50% 40%,#d7ad92,#7a5b45 65%,#c9c6bd)"></div>
    <div class="caption">Clara Meier</div>
  </div>
  <div class="abs member" style="left:518px;top:649px">
    <div class="photo" role="img" aria-label="Close portrait of a dark-haired woman" style="background:radial-gradient(circle at 50% 45%,#e4c2b2,#4a3530 70%,#2d2424)"></div>
    <div class="caption">Nina Roth</div>
  </div>
  <div class="abs member" style="left:671px;top:649px">
    <div class="photo" role="img" aria-label="Portrait of a woman with long brown hair" style="background:radial-gradient(circle at 55% 45%,#e0bfa5,#6b4a35 65%,#f2f2f2)"></div>
    <div class="caption">Sophie Lenz</div>
  </div>

  <div class="abs band"></div>

  <section class="abs welcome">
    <h2>Welcome to Swiss Soirée</h2>
    <p>Claritas est etiam processus dynamicus, qui sequitur mutationem consuetudium lectorum. Mirum est notare quam littera gothica, quam nunc putamus parum claram, anteposuerit litterarum formas humanitatis per seacula quarta decima et quinta decima. Eodem modo typi, qui nunc nobis videntur parum clari, fiant sollemnes in futurum.</p>
    <p>Duis autem vel eum iriure dolor in hendrerit in vulputate velit esse molestie consequat, vel illum dolore eu feugiat nulla facilisis at vero eros et accumsan et iusto odio dignissim qui blandit praesent.</p>
    <a class="register">Register For Free</a>
  </section>

  <section class="abs why">
    <h2>Why you choose us?</h2>
    <p>Ut wisi enim ad minim veniam, quis nostrud exerci tation ullamcorper suscipit lobortis nisl ut aliquip ex ea commodo consequat. Duis autem vel eum iriure dolor.</p>
    <ul>
      <li>Phasellus felis dolor sceler</li>
      <li>Tempus eget lobortisro.</li>
      <li>Aliquam nec erat at purus</li>
      <li>Vestibulum ligula augue</li>
    </ul>
  </section>

  <footer class="abs footer">
    <div class="footer-links">Terms and Conditions | Privacy Promise | FAQ's | Contact Us</div>
    <div class="copyright">Copyright © 2013. All Rights Reserved.</div>
    <div class="social" style="left:629px">
      <span style="left:0;background:#3b5ba5"></span>
      <span style="left:35px;background:#2f9bd6"></span>
      <span style="left:69px;background:#f57f22"></span>
      <span style="left:104px;background:#e2262b"></span>
    </div>
  </footer>

</div>
</body>
</html>
```